Musician looking for catchy Web Design for promotion

My name is Brenna Colfer. I'm an Irish musician who plays the tin whistle and the flute. I'm also the leader of a traditional Irish music and dance ensemble called Wander the Hillside (www.wanderthehillside-example.com) and for the past 30 years, I've toured the world performing thousands of concerts. I run an annual cruise (www.brennacolfervoyage-example.com) that I would like a link to, and I'm also I'm organizing tours to Ireland that I would like a page set up for. I'm looking for a website to promote my tours and my music.
Updates

Hello Graphic Designers, I am only looking for the design of the home page to make my decision. Thank you. Brenna

Target Market(s)

Music fans of Irlsh and World Music

Industry/Entity Type

Entertainment Industry

Number of Pages Required

5+ page

Requirements
Must have
• I'm looking for a catchy design that shows a photo of me. I would like a few links....
• BIO
• TOURDATES
• BRENNA COLFER CRUISE
• MUSICAL TOUR OF IRELAND
• CONTACT
• VIDEO
• GALLERY
• CONTACT
• MAILING LIST
• STORE
Nice to have
• we'll see!

```html
<!DOCTYPE html>
<html lang="en">
<head>
<meta charset="utf-8">
<title>Brenna Colfer – Irish Musician</title>
<link href="https://fonts.googleapis.com/css2?family=Cinzel:wght@400;700&family=Open+Sans:ital,wght@0,400;0,600;0,700;1,400&display=swap" rel="stylesheet">
<style>
:root{
  --black:#1c1c1c;
  --white:#ffffff;
  --gold:#f2bd1a;
  --gold-dark:#d9a70c;
  --panel:#f3f3f3;
  --line:#dcdcdc;
  --text:#555555;
  --heading:#222222;
  --muted:#888888;
  --hero-cream:#d8c49a;
}
*{box-sizing:border-box;margin:0;padding:0}
html,body{width:1200px;height:2335px;overflow:hidden}
body{background:var(--white);font-family:"Open Sans",Arial,sans-serif;color:var(--text);position:relative}
a{color:inherit;text-decoration:none}

/* nav */
.top-nav{position:absolute;left:0;top:0;width:1200px;height:48px;background:var(--black);display:flex;align-items:center;padding-left:98px}
.top-nav a{color:var(--white);font-size:13px;font-weight:600;text-transform:uppercase;margin-right:32px;letter-spacing:.2px;white-space:nowrap}
.top-nav a.active{color:var(--gold)}

/* header */
.site-header{position:absolute;top:48px;left:0;width:1200px;height:102px}
.brand{position:absolute;left:60px;top:30px;display:flex;align-items:center;gap:10px}
.brand-mark{width:16px;height:16px;background:var(--black);border-radius:50%}
.brand-name{font-family:"Cinzel",serif;font-size:17px;font-weight:700;color:var(--black);line-height:1.1}
.search{position:absolute;left:767px;top:27px;width:333px;height:48px;border:1px solid #cfcfcf;border-radius:3px;display:flex;align-items:center;padding:0 18px;justify-content:space-between}
.search span{font-size:12px;color:#999;letter-spacing:.5px}

/* hero */
.hero{position:absolute;top:150px;left:0;width:1200px;height:440px;background:linear-gradient(90deg,#7b2416 0%,#a53a22 20%,var(--hero-cream) 45%,#a33620 65%,#7b2416 100%)}
.hero-portrait{position:absolute;left:124px;top:-7px;width:371px;height:445px;border-radius:50%;border:5px solid var(--white);background:radial-gradient(ellipse at 50% 40%,#9b7350 0%,#4a2e1c 55%,#2a1a10 100%)}
.hero-title{position:absolute;left:530px;top:150px;width:600px;text-align:center;font-family:"Cinzel",serif;color:var(--white);font-size:64px;font-weight:400;line-height:1;white-space:nowrap;text-shadow:0 3px 8px rgba(0,0,0,.6)}
.hero-sub{position:absolute;left:530px;top:250px;width:600px;text-align:center;color:var(--white);font-size:27px;line-height:1.2;text-transform:uppercase;white-space:nowrap;text-shadow:0 2px 6px rgba(0,0,0,.6)}
.dots{position:absolute;left:564px;top:385px;display:flex;gap:5px}
.dots i{width:16px;height:16px;border-radius:50%;border:2px solid var(--white);display:block}
.dots i.on{background:var(--gold);border-color:var(--gold)}

/* shared */
.panel{position:absolute;background:var(--panel)}
.section-title{font-family:"Cinzel",serif;color:var(--heading);line-height:1.15;font-weight:400}
.section-title small{display:block;font-size:15px;font-weight:400}
.section-title b{font-weight:400;font-size:23px;display:block}
.ornament{display:inline-block;width:44px;height:34px;background:linear-gradient(135deg,#bbb,#555);border-radius:4px;vertical-align:middle}
.more{color:var(--gold);font-weight:700;font-size:12px;text-transform:uppercase}

/* welcome */
.welcome{left:98px;top:590px;width:537px;height:219px;padding:30px 30px}
.welcome .ornament{position:absolute;left:232px;top:22px}
.welcome p{margin-top:26px;font-size:11.5px;line-height:2.1}

/* video */
.video{position:absolute;left:98px;top:809px;width:537px;height:349px;background:linear-gradient(180deg,#8fb2cf 0%,#c9b79a 45%,#8b6e57 75%,#5c4a3e 100%)}
.video .play-big{position:absolute;left:238px;top:150px;width:56px;height:56px;border-radius:50%;background:rgba(0,0,0,.55)}
.video-tools{position:absolute;right:10px;top:22px;display:flex;flex-direction:column;gap:6px}
.video-tools span{width:30px;height:30px;background:rgba(0,0,0,.75);display:flex;align-items:center;justify-content:center}
.video-bar{position:absolute;left:20px;right:20px;bottom:20px;height:40px;display:flex;align-items:center;gap:8px}
.video-bar .btn{width:62px;height:40px;background:rgba(0,0,0,.8);display:flex;align-items:center;justify-content:center}
.video-bar .track{flex:1;height:40px;background:rgba(0,0,0,.8);display:flex;align-items:center;padding:0 10px;gap:10px;color:var(--white);font-size:12px;font-weight:700;position:relative}
.video-bar .track em{position:absolute;left:0;top:-22px;background:#222;color:#fff;font-style:normal;font-size:11px;padding:1px 5px}
.video-bar .line{flex:1;height:8px;background:#777}

/* critics */
.critics{left:98px;top:1158px;width:537px;height:726px;padding:40px 30px 0}
.critics .ornament{position:absolute;left:300px;top:26px}
.quote{position:absolute;left:22px;width:493px;height:140px;border-bottom:1px solid var(--line);display:flex;align-items:center;gap:24px;padding-left:8px}
.quote .avatar{width:92px;height:92px;border-radius:50%;border:3px solid var(--white);box-shadow:0 0 0 1px #ddd;flex:none}
.quote p{font-size:11.5px;line-height:2;color:var(--text)}
.quote cite{display:block;font-style:italic;color:#333;margin-top:6px}
.view-more{position:absolute;right:24px;bottom:22px}

/* adventure */
.adventure{position:absolute;left:675px;top:590px;width:425px;height:154px;background:var(--gold);padding:22px 25px}
.adventure h2{font-family:"Cinzel",serif;font-weight:400;color:var(--white);font-size:22px}
.adventure p{color:var(--white);font-size:11px;margin-top:8px}
.adventure .book{display:inline-block;margin-top:14px;background:linear-gradient(#f4f4f4,#d8d8d8);color:#333;font-weight:700;font-size:13px;padding:10px 20px;border-radius:3px;text-transform:uppercase}

/* music */
.music{left:675px;top:744px;width:425px;height:624px}
.music .section-title{position:absolute;left:35px;top:40px}
.music .ornament{position:absolute;left:72px;top:24px}
.music-meta{position:absolute;left:18px;right:18px;top:127px;display:flex;justify-content:space-between;font-size:11px;color:#666;text-transform:uppercase}
.music-art{position:absolute;left:0;top:149px;width:425px;height:263px;background:linear-gradient(180deg,#b9c4c6 0%,#8c8a86 40%,#6b5a4a 70%,#3b3a30 100%)}
.player{position:absolute;left:34px;right:34px;bottom:22px}
.player .bar{height:5px;background:var(--white);position:relative}
.player .bar i{position:absolute;left:0;top:0;width:38px;height:5px;background:#d62e2e}
.player .bar b{position:absolute;left:32px;top:-5px;width:14px;height:14px;border-radius:50%;background:#ccc}
.player .ctrl{display:flex;justify-content:space-between;align-items:center;margin-top:14px;color:var(--white);font-size:12px}
.tracks{position:absolute;left:25px;right:25px;top:428px;list-style:none}
.tracks li{display:flex;justify-content:space-between;font-size:11.5px;color:#666;height:43px;align-items:center;border-bottom:1px solid var(--line)}
.tracks li:last-child{border-bottom:none}
.divider{position:absolute;left:675px;top:1364px;width:425px;height:6px;background:#d6d6d6}

/* tours */
.tours{left:675px;top:1370px;width:425px;height:514px}
.tours .section-title{position:absolute;left:35px;top:55px}
.tours .ornament{position:absolute;left:72px;top:30px}
.tour-table{position:absolute;left:0;top:121px;width:425px;border-collapse:collapse;font-size:12px;color:#555;text-align:center}
.tour-table th{background:var(--gold);color:var(--white);font-weight:700;height:44px;text-transform:uppercase;font-size:12px;border-right:1px solid var(--gold-dark)}
.tour-table td{height:46px;border-bottom:1px solid var(--line);border-right:1px solid var(--line);line-height:1.5}
.tour-table td:last-child,.tour-table th:last-child{border-right:none}
.tour-table tr.tall td{height:80px}

/* newsletter */
.newsletter{left:98px;top:1925px;width:1002px;height:202px;text-align:center}
.newsletter .section-title{position:absolute;left:0;right:0;top:40px}
.newsletter .ornament{position:absolute;left:558px;top:20px}
.signup{position:absolute;left:136px;top:112px;display:flex;gap:26px}
.signup .field{width:556px;height:48px;background:var(--white);border:1px solid #ccc;border-radius:2px;font-size:12px;color:#777;display:flex;align-items:center;padding-left:18px;text-transform:uppercase}
.signup .go{width:148px;height:52px;background:var(--gold);color:var(--white);font-weight:700;font-size:15px;display:flex;align-items:center;justify-content:center;border-radius:2px;text-transform:uppercase}

/* footer */
.site-footer{position:absolute;left:0;top:2171px;width:1200px;height:164px;background:var(--black);color:var(--white);text-align:center}
.social{margin-top:34px;display:flex;justify-content:center;gap:22px;font-size:12px;font-weight:700}
.footer-links{margin-top:26px;font-size:12px}
.footer-links a{padding:0 6px}
.copy{margin-top:22px;font-size:12px}
</style>
</head>
<body>

<nav class="top-nav">
  <a class="active" href="#">Home</a><a href="#">Bio</a><a href="#">Tourdates</a><a href="#">Brenna Colfer Cruise</a><a href="#">Musical Tour of Ireland</a><a href="#">Video</a><a href="#">Gallery</a><a href="#">Contact</a><a href="#">Mailing List</a><a href="#">Store</a>
</nav>

<header class="site-header">
  <div class="brand"><span class="brand-mark"></span><span class="brand-name">Brenna Colfer's<br>Musical Tour of Ireland</span></div>
  <div class="search"><span>SEARCH</span>
    <svg width="18" height="18" viewBox="0 0 18 18"><circle cx="7.5" cy="7.5" r="5.5" fill="none" stroke="#999" stroke-width="2"/><line x1="11.5" y1="11.5" x2="16" y2="16" stroke="#999" stroke-width="2.5"/></svg>
  </div>
</header>

<section class="hero">
  <div class="hero-portrait" role="img" aria-label="Portrait photo of Brenna Colfer holding a flute"></div>
  <h1 class="hero-title">Brenna Colfer</h1>
  <p class="hero-sub">Irish Musician</p>
  <div class="dots"><i class="on"></i><i></i><i></i><i></i></div>
</section>

<section class="panel welcome">
  <h2 class="section-title"><small>Welcome to</small><b>Brenna Colfer</b></h2>
  <span class="ornament" role="img" aria-label="Tin whistle ornament"></span>
  <p>BRENNA COLFER is considered one of the greatest musicians and personalities in the history of Irish music in America. She was born in the Bronx, New York of Irish parents, and she is the second oldest of seven children.. <a class="more" href="#">Read more &gt;&gt;</a></p>
</section>

<section class="video" role="img" aria-label="Video still of a street with an orange tram">
  <div class="video-tools">
    <span><svg width="16" height="14" viewBox="0 0 16 14"><path d="M8 13 1.5 6.5A3.5 3.5 0 0 1 8 2a3.5 3.5 0 0 1 6.5 4.5Z" fill="#fff"/></svg></span>
    <span><svg width="14" height="14" viewBox="0 0 14 14"><path d="M13 1 1 6l5 2 2 5Z" fill="#fff"/></svg></span>
  </div>
  <div class="play-big"><svg width="56" height="56" viewBox="0 0 56 56"><path d="M23 18v20l16-10Z" fill="#fff"/></svg></div>
  <div class="video-bar">
    <div class="btn"><svg width="16" height="18" viewBox="0 0 16 18"><path d="M1 1v16l14-8Z" fill="#fff"/></svg></div>
    <div class="track"><em>02:33</em><span class="line"></span><span>HD</span><span>Reelhost</span></div>
  </div>
</section>

<section class="panel critics">
  <h2 class="section-title"><small>What the critics are saying</small><b>About Brenna Colfer....</b></h2>
  <span class="ornament" role="img" aria-label="Tin whistle ornament"></span>
  <div class="quote" style="top:84px"><span class="avatar" role="img" aria-label="Photo of a glass building" style="background:radial-gradient(#c8dbe2,#4f6b3a)"></span><p>"When distinguished tin whistle or flute players over the past quarter of a century come to mind, ... <a class="more" href="#">Read more &gt;&gt;</a><cite>- Dermot Fallon, The Harbour Ledger</cite></p></div>
  <div class="quote" style="top:224px"><span class="avatar" role="img" aria-label="Photo of a dandelion" style="background:radial-gradient(#f2f2f2,#8a8e8e)"></span><p>"Brenna Colfer is one of New York's finest flute and whistle players, not to mention the only American ... <a class="more" href="#">Read more &gt;&gt;</a><cite>- Siobhan Tierney, The Liffey Courier (Dublin)</cite></p></div>
  <div class="quote" style="top:364px"><span class="avatar" role="img" aria-label="Photo of a sunset over water" style="background:radial-gradient(#fff3d8,#a8876a)"></span><p>"Colfer has become a preeminent Irish flute and whistle virtuoso, constantly in demand for session... <a class="more" href="#">Read more &gt;&gt;</a><cite>- Warren Pike, The Bayside Herald</cite></p></div>
  <div class="quote" style="top:504px"><span class="avatar" role="img" aria-label="Photo of a person walking among trees" style="background:radial-gradient(#e8dde8,#6a5a7a)"></span><p>"Brenna is among the most brilliant whistle players ever recorded. Her compositions, mostly ... <a class="more" href="#">Read more &gt;&gt;</a><cite>- Colm Darragh, The Emerald Post</cite></p></div>
  <a class="more view-more" href="#">View more &gt;&gt;</a>
</section>

<section class="adventure">
  <h2>An Adventure Awaits You</h2>
  <p>At vero eos et accusamus et iusto odio dignissimos ducim.</p>
  <a class="book" href="#">Book now</a>
</section>

<section class="panel music">
  <span class="ornament" role="img" aria-label="Tin whistle ornament"></span>
  <h2 class="section-title"><small>My</small><b>Music</b></h2>
  <div class="music-meta"><span>Album 1</span><span>&#8635; Repeat &nbsp;| &nbsp;Share</span></div>
  <div class="music-art" role="img" aria-label="Album art of snowy mountains">
    <div class="player">
      <div class="bar"><i></i><b></b></div>
      <div class="ctrl">
        <svg width="80" height="14" viewBox="0 0 80 14"><circle cx="7" cy="7" r="6" fill="#fff"/><path d="M5 4v6l5-3Z" fill="#333"/><rect x="20" y="1" width="4" height="12" fill="#fff"/><rect x="27" y="1" width="4" height="12" fill="#fff"/><rect x="40" y="1" width="12" height="12" fill="#fff"/><path d="M62 5h3l4-4v12l-4-4h-3Z" fill="#fff"/></svg>
        <span>00:00 / 00:00</span>
      </div>
    </div>
  </div>
  <ul class="tracks">
    <li><span>Album 1</span><span>2:30</span></li>
    <li><span>Album 2</span><span>5:06</span></li>
    <li><span>Album 3</span><span>3:00</span></li>
    <li><span>Album 4</span><span>4:30</span></li>
  </ul>
</section>
<div class="divider"></div>

<section class="panel tours">
  <span class="ornament" role="img" aria-label="Tin whistle ornament"></span>
  <h2 class="section-title"><small>My</small><b>Tours</b></h2>
  <table class="tour-table">
    <thead><tr><th>Day</th><th>Port</th><th>Timing</th></tr></thead>
    <tbody>
      <tr><td>Sunday</td><td>Newyork</td><td>4:00pm</td></tr>
      <tr><td>Monday</td><td>At Sea</td><td></td></tr>
      <tr class="tall"><td>Wednesday</td><td>Saint John, Bay<br>of Fundy, New<br>Brunswick</td><td>11:00am - 7:00pm</td></tr>
      <tr><td>Thursday</td><td>Portland, Maine</td><td>8:00am - 5:00pm</td></tr>
      <tr><td>Friday</td><td>At Sea</td><td></td></tr>
      <tr><td>Saturday</td><td>Newyork</td><td>8:00am</td></tr>
    </tbody>
  </table>
</section>

<section class="panel newsletter">
  <span class="ornament" role="img" aria-label="Tin whistle ornament"></span>
  <h2 class="section-title"><small>Join our</small><b>Newsletter</b></h2>
  <div class="signup"><div class="field">Email address</div><a class="go" href="#">Subscribe</a></div>
</section>

<footer class="site-footer">
  <div class="social"><span>Facenook</span><span>Chirper</span><span>Circlely</span><span>Linkwork</span><span>Snapgram</span><span>Pinboard</span><span>Feedline</span></div>
  <div class="footer-links"><a href="#">Home</a>|<a href="#">Bio</a>|<a href="#">Tourdates</a>|<a href="#">Brenna Colfer Cruise</a>|<a href="#">Musical Tour Of Ireland</a>|<a href="#">Video</a>|<a href="#">Gallery</a>|<a href="#">Contact</a>|<a href="#">Mailing List</a>|<a href="#">Store</a></div>
  <p class="copy">Copyrights © 2016, Brenna Colfer. All rights reserved.</p>
</footer>

</body>
</html>
```